Word Template for Communications, Reports

I. A Word template for External Reports and a Word template for External Communications
1.Create a template in Word for reports and another template in Word for sending external communications.
1.1. Predefined and locked text styles.
1.2. Quick elements fields (custom) that allow the integration of basic information of each document.
1.3. Professional design and that administrators can place it to different projects.

II. Job postings
We also want a template in Word to make vacancy postings, to facilitate the job of recruiting staff.
Updates

Target Market(s)

External clients (our main clients are public institutions of the government of the Dominican Republic.)

Industry/Entity Type

Construcción

Font styles to use
Serif
Other font styles liked:
• Arial, Book Antiqua

Colors
EE7325
F08F49
F5BC92
FAE3D3
FDF4ED
EB3D1F
EC4F4E
F09395
F8D3D4
FCEDEE

Requirements
Nice to have
• Since we are a group of about 4 companies, I would like each template to be used by any of the companies

```html
<!DOCTYPE html>
<html lang="en">
<head>
<meta charset="utf-8">
<title>Korvel Letterhead and Communication Material</title>
<link href="https://fonts.googleapis.com/css2?family=Poppins:wght@400;500;600;700;800&display=swap" rel="stylesheet">
<style>
  :root {
    --canvas-grey: #c8c9cb;
    --paper: #ffffff;
    --ink: #111111;
    --brand-red: #bf1e24;
    --brand-red-deep: #8e1216;
    --accent-red: #e3161b;
    --black: #000000;
  }
  * { box-sizing: border-box; margin: 0; padding: 0; }
  html, body { width: 1200px; height: 915px; overflow: hidden; }
  body {
    position: relative;
    background: var(--canvas-grey);
    font-family: "Poppins", sans-serif;
    color: var(--ink);
  }

  /* ---------- Letterhead ---------- */
  .letterhead {
    position: absolute;
    left: 74.6px; top: 170.4px;
    width: 406.2px; height: 574.4px;
    background: var(--paper);
  }
  .letterhead__brand {
    position: absolute;
    left: 29px; top: 36px;
    font-weight: 800;
    font-size: 30px;
    letter-spacing: 3px;
    line-height: 1;
    color: var(--ink);
  }
  .letterhead__tagline {
    position: absolute;
    right: 33.6px; top: 31px;
    text-align: right;
    font-weight: 600;
    font-size: 9.6px;
    line-height: 11.6px;
  }
  .letterhead__tagline .is-red { color: var(--accent-red); }
  .meta-field {
    position: absolute;
    top: 83px;
    font-size: 7px;
    display: flex;
    align-items: flex-end;
  }
  .meta-field__line {
    display: inline-block;
    border-bottom: 0.6px solid var(--ink);
    width: 56px;
    height: 7px;
    margin-left: 2px;
  }
  .meta-field--date { left: 29px; }
  .meta-field--ref { right: 33.6px; }
  .letterhead__salutation {
    position: absolute;
    left: 29px; top: 129px;
    font-weight: 500;
    font-size: 9.6px;
  }
  .letterhead__body {
    position: absolute;
    left: 29px; top: 148px;
    width: 343.6px;
    font-size: 6.9px;
    line-height: 15.1px;
  }
  .letterhead__line {
    display: block;
    white-space: nowrap;
    text-align: justify;
    text-align-last: justify;
  }
  .letterhead__line--end { text-align-last: left; }
  .letterhead__signature {
    position: absolute;
    left: 31px; top: 361px;
    width: 48px; height: 23px;
    border-radius: 4px;
    background: linear-gradient(90deg, rgba(191,30,36,0.18), rgba(191,30,36,0.08));
  }
  .letterhead__footer {
    position: absolute;
    left: 0; right: 0; top: 534.2px;
    height: 24.5px;
    background: var(--black);
    color: var(--paper);
    font-size: 7.2px;
    display: flex; align-items: center; justify-content: center;
  }

  /* ---------- Communication material board ---------- */
  .board-shadow {
    position: absolute;
    left: 533.6px; top: 653.4px;
    width: 574.4px; height: 28px;
  }
  .board {
    position: absolute;
    left: 533.6px; top: 247.2px;
    width: 574.4px; height: 406.2px;
    background: var(--brand-red);
    overflow: hidden;
  }
  .board__header {
    position: absolute;
    left: 0; top: 0; right: 0;
    height: 53px;
    background: var(--brand-red-deep);
    border-radius: 0 0 28px 28px;
    display: flex; align-items: center; justify-content: center;
  }
  .board__title {
    color: var(--paper);
    font-weight: 700;
    font-size: 27px;
    letter-spacing: 0.2px;
    padding-top: 8px;
  }
  .plan-table {
    position: absolute;
    left: 29.4px; top: 66.8px;
    display: grid;
    grid-template-columns: 73.5px 80px 80px 79.6px 101.8px 79.7px;
    grid-template-rows: 27px repeat(7, 32.6px);
    column-gap: 4.1px;
    row-gap: 3.2px;
  }
  .plan-table__head, .plan-table__cell {
    border-radius: 5px;
    display: flex; align-items: center; justify-content: center;
    text-align: center;
    font-weight: 700;
  }
  .plan-table__head {
    color: var(--paper);
    font-size: 6px;
    line-height: 7.2px;
  }
  .plan-table__head--red { background: var(--brand-red-deep); }
  .plan-table__head--black { background: var(--black); }
  .plan-table__cell {
    background: var(--paper);
    color: var(--ink);
    font-size: 5.8px;
  }
  .plan-table__cell--situation { font-weight: 600; }
  .plan-table__cell--situation-dark {
    background: var(--brand-red-deep);
    color: var(--paper);
  }
  .board__footer {
    position: absolute;
    left: 0; right: 0; bottom: 0;
    height: 44.6px;
    background: var(--black);
    border-radius: 32px 32px 0 0;
    display: flex; align-items: center; justify-content: center;
  }
  .board__brand {
    color: var(--paper);
    font-weight: 800;
    font-size: 22px;
    letter-spacing: 3px;
    line-height: 1;
    padding-bottom: 3px;
  }
</style>
</head>
<body>

  <section class="letterhead">
    <div class="letterhead__brand">KORVEL</div>
    <div class="letterhead__tagline">
      SANITARY<br>
      <span class="is-red">INFRASTRUCTURE</span><br>
      WORKS
    </div>

    <div class="meta-field meta-field--date">Date:<span class="meta-field__line"></span></div>
    <div class="meta-field meta-field--ref">Ref:<span class="meta-field__line"></span></div>

    <p class="letterhead__salutation">Dear, Korvel</p>

    <div class="letterhead__body">
      <span class="letterhead__line">Lorem ipsum dolor sit amet, consectetuer adipiscing elit, sed diam nonummy nibh euismod</span>
      <span class="letterhead__line">tincidunt ut laoreet dolore magna aliquam erat volutpat. Ut wisi enim ad minim veniam, quis</span>
      <span class="letterhead__line">nostrud exerci tation ullamcorper suscipit lobortis nisl ut aliquip ex ea commodo consequat. Duis</span>
      <span class="letterhead__line">autem vel eum iriure dolor in hendrerit in vulputate velit esse molestie consequat, vel illum dolore</span>
      <span class="letterhead__line">eu feugiat nulla facilisis at vero eros et accumsan et iusto odio dignissim qui blandit praesent</span>
      <span class="letterhead__line letterhead__line--end">luptatum zzril delenit augue duis dolore te feugait nulla facilisi.</span>
      <span class="letterhead__line">Lorem ipsum dolor sit amet, cons ectetuer adipiscing elit, sed diam nonummy nibh euismod</span>
      <span class="letterhead__line">tincidunt ut laoreet dolore magna aliquam erat volutpat. Ut wisi enim ad minim veniam, quis</span>
      <span class="letterhead__line letterhead__line--end">nostrud exerci tation ullamcorper suscipit lobortis nisl ut aliquip ex ea commodo consequat.</span>
      <span class="letterhead__line">Lorem ipsum dolor sit amet, consectetuer adipiscing elit, sed diam nonummy nibh euismod</span>
      <span class="letterhead__line">tincidunt ut laoreet dolore magna aliquam erat volutpat. Ut wisi enim ad minim veniam, quis</span>
      <span class="letterhead__line">nostrud exerci tation ullamcorper suscipit lobortis nisl ut aliquip ex ea commodo consequat. Duis</span>
      <span class="letterhead__line letterhead__line--end">autem vel eum iriure dolor in hendrerit in .</span>
    </div>

    <div class="letterhead__signature" role="img" aria-label="Handwritten signature in red ink"></div>

    <footer class="letterhead__footer">48 Meridian Ave. Lakeview, NJ 07390 | P: 10-555-0142 | F: 732-555-0168</footer>
  </section>

  <svg class="board-shadow" viewBox="0 0 574.4 28" preserveAspectRatio="none" aria-hidden="true">
    <defs>
      <linearGradient id="boardShadowFade" x1="0" y1="0" x2="0" y2="1">
        <stop offset="0" stop-color="#8f9092"/>
        <stop offset="1" stop-color="#c8c9cb"/>
      </linearGradient>
    </defs>
    <polygon points="0,0 574.4,0 574.4,28 287.2,5.5 0,28" fill="url(#boardShadowFade)"/>
  </svg>

  <section class="board">
    <header class="board__header">
      <h1 class="board__title">COMMUNICATION MATERIAL</h1>
    </header>

    <div class="plan-table">
      <div class="plan-table__head plan-table__head--red">Communication<br>Plan Situation</div>
      <div class="plan-table__head plan-table__head--black">Level of<br>Urgency (1-4)</div>
      <div class="plan-table__head plan-table__head--red">Stakeholder(s)<br>DRI</div>
      <div class="plan-table__head plan-table__head--black">Objectives<br>and Goals</div>
      <div class="plan-table__head plan-table__head--red">Required Actions,<br>Messaging &amp; Content</div>
      <div class="plan-table__head plan-table__head--black">Due Date</div>

      <div class="plan-table__cell plan-table__cell--situation">One</div>
      <div class="plan-table__cell">TEXT HERE</div><div class="plan-table__cell">TEXT HERE</div><div class="plan-table__cell">TEXT HERE</div><div class="plan-table__cell">TEXT HERE</div><div class="plan-table__cell">TEXT HERE</div>

      <div class="plan-table__cell plan-table__cell--situation plan-table__cell--situation-dark">Two</div>
      <div class="plan-table__cell">TEXT HERE</div><div class="plan-table__cell">TEXT HERE</div><div class="plan-table__cell">TEXT HERE</div><div class="plan-table__cell">TEXT HERE</div><div class="plan-table__cell">TEXT HERE</div>

      <div class="plan-table__cell plan-table__cell--situation">Three</div>
      <div class="plan-table__cell">TEXT HERE</div><div class="plan-table__cell">TEXT HERE</div><div class="plan-table__cell">TEXT HERE</div><div class="plan-table__cell">TEXT HERE</div><div class="plan-table__cell">TEXT HERE</div>

      <div class="plan-table__cell plan-table__cell--situation plan-table__cell--situation-dark">Four</div>
      <div class="plan-table__cell">TEXT HERE</div><div class="plan-table__cell">TEXT HERE</div><div class="plan-table__cell">TEXT HERE</div><div class="plan-table__cell">TEXT HERE</div><div class="plan-table__cell">TEXT HERE</div>

      <div class="plan-table__cell plan-table__cell--situation">Five</div>
      <div class="plan-table__cell">TEXT HERE</div><div class="plan-table__cell">TEXT HERE</div><div class="plan-table__cell">TEXT HERE</div><div class="plan-table__cell">TEXT HERE</div><div class="plan-table__cell">TEXT HERE</div>

      <div class="plan-table__cell plan-table__cell--situation plan-table__cell--situation-dark">Six</div>
      <div class="plan-table__cell">TEXT HERE</div><div class="plan-table__cell">TEXT HERE</div><div class="plan-table__cell">TEXT HERE</div><div class="plan-table__cell">TEXT HERE</div><div class="plan-table__cell">TEXT HERE</div>

      <div class="plan-table__cell plan-table__cell--situation">Seven</div>
      <div class="plan-table__cell">TEXT HERE</div><div class="plan-table__cell">TEXT HERE</div><div class="plan-table__cell">TEXT HERE</div><div class="plan-table__cell">TEXT HERE</div><div class="plan-table__cell">TEXT HERE</div>
    </div>

    <footer class="board__footer">
      <div class="board__brand">KORVEL</div>
    </footer>
  </section>

</body>
</html>
```